Brightfield Co Trade Show Flyer

We need a brochure design (8.5 x 11) Info in the design (refer to rough draft I drew on Paper): "#1 selling tool to aquire new franchisees has been video testimonials" - Martin L. Crowe, C.E.O Tovik Smoothie Franchise Testimonials - Let your franchisees do the selling for you. Franchisee testimonial: $10,000 / per Franchisee Includes: • 2 minute Video • 1 minute add for your franchise's location • Concept creation • Communication with franchisee • Travel to their location • All rental equipment • 1 round of corrections • Animated logo • Licensed music ******* For 25% Discount section (next to middle box), please put the "Outlet Summit Logo" Great to use on all your social media (USE logos and icons) • Website • ClipStream • WorkLink • Friendwall • SnapFrame • Chirper • Phone calls • Emails • In person meetings Some of our clients: (use the logos I uploaded - in round boxes as in draft) LOGO (Brightfield Franchise Testimonial) www.brightfieldvoices.example (866) 555-0172

Target Market(s)

Franchise owners

Colors

Designer to choose colors to be used in the design.

Requirements

```html
<!DOCTYPE html>
<html lang="en">
<head>
<meta charset="utf-8">
<title>Brightfield Co – Franchise Testimonials Flyer</title>
<link href="https://fonts.googleapis.com/css2?family=Arimo:wght@400;700&display=swap" rel="stylesheet">
<style>
  :root {
    --page: #d9d9d9;
    --flyer: #2f2d2e;
    --red: #e8373a;
    --white: #ffffff;
    --ink: #2f2d2e;
  }
  * { box-sizing: border-box; margin: 0; padding: 0; }
  html, body { width: 1200px; height: 1200px; overflow: hidden; }
  body { background: var(--page); font-family: "Arimo", Arial, sans-serif; }
  .flyer {
    position: absolute; left: 159px; top: 30px; width: 882px; height: 1140px;
    background: var(--flyer); color: var(--white);
    box-shadow: 0 8px 24px rgba(0,0,0,.3);
  }
  .abs { position: absolute; }
  .quote {
    left: 24px; top: 27px; width: 835px; height: 77px;
    border: 1.5px solid var(--red); border-radius: 5px;
    font-size: 24px; text-align: center; padding-top: 17px;
  }
  .quote-source {
    left: 0; width: 882px; top: 90px; text-align: center; font-size: 19px;
  }
  .quote-source span { background: var(--flyer); padding: 0 14px; }
  .headline-main {
    left: 0; width: 882px; top: 125px; text-align: center;
    color: var(--red); font-weight: 700; font-size: 98px; line-height: 1; letter-spacing: 1px;
  }
  .headline-sub {
    left: 0; width: 882px; top: 218px; text-align: center;
    font-size: 82px; font-weight: 400; line-height: 1; letter-spacing: 1px;
  }
  .tagline {
    left: 0; width: 882px; top: 312px; text-align: center;
    color: var(--red); font-size: 26px;
  }
  .includes {
    left: 94px; top: 368px; width: 520px; height: 298px;
    border: 1.5px dashed var(--red); border-right: none; border-radius: 6px 0 0 6px;
    padding: 14px 0 0 26px; list-style: none;
  }
  .includes li { font-size: 20.5px; height: 29.3px; display: flex; align-items: center; gap: 14px; }
  .includes svg { width: 16px; height: 16px; flex: none; }
  .discount {
    left: 614px; top: 368px; width: 187px; height: 298px; background: var(--red);
    padding: 14px 0 0 20px; color: var(--ink);
  }
  .discount-note { font-size: 22px; line-height: 1; }
  .discount-rate { font-size: 78px; font-weight: 700; line-height: .95; letter-spacing: -3px; margin-top: 6px; }
  .discount-label { font-size: 28px; line-height: 1; }
  .summit-name {
    margin-top: 18px; font-size: 22px; line-height: 1.1; color: var(--white);
  }
  .everywhere {
    left: 0; width: 882px; top: 690px; text-align: center; font-size: 27px; font-weight: 700; color: var(--red);
  }
  .everywhere b { color: var(--white); }
  .channel {
    width: 56px; height: 56px; top: 742px; border-radius: 50%;
    background: var(--white); border: 3px solid var(--red);
    display: flex; align-items: center; justify-content: center;
    color: var(--ink); font-size: 9px; font-weight: 700; text-align: center;
  }
  .channel.dark { background: var(--flyer); }
  .channel svg { width: 30px; height: 30px; }
  .clients-title {
    left: 0; width: 882px; top: 829px; text-align: center; font-size: 16px; font-weight: 700;
  }
  .client {
    width: 78px; height: 78px; top: 875px; border-radius: 50%;
    background: var(--white); border: 3px solid var(--red);
    display: flex; align-items: center; justify-content: center;
    color: var(--red); font-size: 11px; font-weight: 700; text-align: center; line-height: 1.1;
  }
  .brand {
    left: 80px; top: 1012px; width: 256px; text-align: center;
  }
  .brand-name { font-size: 31px; font-weight: 700; letter-spacing: 1px; }
  .brand-line { font-size: 11px; margin-top: 6px; letter-spacing: .5px; }
  .divider { left: 346px; top: 1000px; width: 2px; height: 120px; background: var(--white); }
  .contact-row { left: 366px; display: flex; align-items: center; gap: 14px; }
  .phone-row { top: 1003px; }
  .web-row { top: 1068px; }
  .phone { color: var(--red); font-size: 45px; font-weight: 700; }
  .web { color: var(--red); font-size: 22px; }
</style>
</head>
<body>
<main class="flyer">
  <p class="abs quote">"#1 selling tool to aquire new franchisees has been video testimonials"</p>
  <p class="abs quote-source"><span>Martin L. Crowe, C.E.O Tovik Smoothie</span></p>

  <h1 class="abs headline-main">FRANCHISE</h1>
  <h2 class="abs headline-sub">TESTIMONIALS</h2>
  <p class="abs tagline">LET YOUR FRANCHISEES DO THE SELLING FOR YOU</p>

  <ul class="abs includes">
    <li><svg viewBox="0 0 16 16"><path d="M2 8l4 4 8-9" fill="none" stroke="#e8373a" stroke-width="2.5"/></svg>$10,000 / per Franchisee</li>
    <li><svg viewBox="0 0 16 16"><path d="M2 8l4 4 8-9" fill="none" stroke="#e8373a" stroke-width="2.5"/></svg>2 minute Video</li>
    <li><svg viewBox="0 0 16 16"><path d="M2 8l4 4 8-9" fill="none" stroke="#e8373a" stroke-width="2.5"/></svg>1 minute add for your franchise's location</li>
    <li><svg viewBox="0 0 16 16"><path d="M2 8l4 4 8-9" fill="none" stroke="#e8373a" stroke-width="2.5"/></svg>Concept creation</li>
    <li><svg viewBox="0 0 16 16"><path d="M2 8l4 4 8-9" fill="none" stroke="#e8373a" stroke-width="2.5"/></svg>Communication with franchisee</li>
    <li><svg viewBox="0 0 16 16"><path d="M2 8l4 4 8-9" fill="none" stroke="#e8373a" stroke-width="2.5"/></svg>Travel to their location</li>
    <li><svg viewBox="0 0 16 16"><path d="M2 8l4 4 8-9" fill="none" stroke="#e8373a" stroke-width="2.5"/></svg>All rental equipment</li>
    <li><svg viewBox="0 0 16 16"><path d="M2 8l4 4 8-9" fill="none" stroke="#e8373a" stroke-width="2.5"/></svg>1 round of corrections</li>
    <li><svg viewBox="0 0 16 16"><path d="M2 8l4 4 8-9" fill="none" stroke="#e8373a" stroke-width="2.5"/></svg>Animated logo</li>
  </ul>

  <section class="abs discount">
    <p class="discount-note">Licensed<br>music *******</p>
    <p class="discount-rate">25%</p>
    <p class="discount-label">DISCOUNT</p>
    <p class="summit-name">The Outlet<br>Summit</p>
  </section>

  <p class="abs everywhere">USE YOUR <b>TESIMONIALS</b> EVERYWHERE</p>

  <div class="abs channel" style="left:105px">Friendwall</div>
  <div class="abs channel" style="left:192px">ClipStream</div>
  <div class="abs channel" style="left:279px">SnapFrame</div>
  <div class="abs channel" style="left:366px">Chirper</div>
  <div class="abs channel" style="left:453px">WorkLink</div>
  <div class="abs channel dark" style="left:540px" aria-label="Email">
    <svg viewBox="0 0 30 30"><rect x="6" y="9" width="18" height="12" fill="#fff"/><path d="M6 9l9 7 9-7" fill="none" stroke="#2f2d2e" stroke-width="1.5"/></svg>
  </div>
  <div class="abs channel dark" style="left:627px" aria-label="Phone">
    <svg viewBox="0 0 30 30"><path d="M6 13c0-4 18-4 18 0v2h-5v-2h-8v2H6z" fill="#fff"/><rect x="8" y="15" width="14" height="7" rx="1" fill="#fff"/><circle cx="15" cy="18.5" r="2" fill="#2f2d2e"/></svg>
  </div>
  <div class="abs channel dark" style="left:714px" aria-label="Website">
    <svg viewBox="0 0 30 30" fill="none" stroke="#fff" stroke-width="1.5"><circle cx="15" cy="15" r="9"/><ellipse cx="15" cy="15" rx="4" ry="9"/><path d="M6 15h18M8 10h14M8 20h14"/></svg>
  </div>

  <p class="abs clients-title">IN PERSON MEETINGS SOME OF OUR CLIENTS:</p>
  <div class="abs client" style="left:209px">Scoopwell</div>
  <div class="abs client" style="left:305px">Corner<br>Nine</div>
  <div class="abs client" style="left:401px">Tovik<br>Smoothie</div>
  <div class="abs client" style="left:497px">Tidywork</div>
  <div class="abs client" style="left:593px">Brakeline</div>

  <div class="abs brand">
    <p class="brand-name">BRIGHTFIELD</p>
    <p class="brand-line">FRANCHISE TESTIMONIALS</p>
  </div>
  <div class="abs divider"></div>
  <div class="abs contact-row phone-row">
    <svg width="44" height="44" viewBox="0 0 44 44"><rect width="44" height="44" rx="6" fill="#fff"/><path d="M14 9l6 1 1 8-4 2c2 5 4 7 8 9l3-4 7 2-1 7c-14 1-24-12-23-25z" fill="#2f2d2e"/></svg>
    <span class="phone">(866) 555-0172</span>
  </div>
  <div class="abs contact-row web-row">
    <svg width="28" height="28" viewBox="0 0 30 30" fill="none" stroke="#fff" stroke-width="1.6"><circle cx="15" cy="15" r="11"/><ellipse cx="15" cy="15" rx="5" ry="11"/><path d="M4 15h22M6 9h18M6 21h18"/></svg>
    <span class="web">www.brightfieldvoices.example</span>
  </div>
</main>
</body>
</html>
```